Business Cards and Letterhead for Solo Attorney
Mark Whitfield, Esq., APC
Business Cards and Letterhead for Solo Attorney - Law
Creative Brief
Professional
SEE ADDITIONAL COMMENTS BELOW
742 S. Milbrook Avenue Alder Springs, CA 90000
mark@whitfieldlegal.example
NAME/TITLE SHOULD APPEAR AS FOLLOWS: Mark Whitfield Attorney at Law/Abogado Workers' Compensation Judge (Ret.) It should also have my corporate name somewhere: Mark Whitfield, Esq., APC

```html
<!DOCTYPE html>
<html lang="en">
<head>
<meta charset="utf-8">
<title>Mark Whitfield, Esq., APC — Stationery</title>
<link href="https://fonts.googleapis.com/css2?family=Open+Sans:wght@400;600;700&display=swap" rel="stylesheet">
<style>
:root{
  --navy:#1f2f6b;
  --gold:#d9a933;
  --paper:#ffffff;
  --ink:#4a4a4a;
  --muted:#8a8a8a;
  --backdrop:#8b8b8b;
  --backdrop-edge:#6f6f6f;
  --shadow:0 3px 8px rgba(0,0,0,.35);
}
*{box-sizing:border-box;margin:0;padding:0}
html,body{width:1200px;height:762px;overflow:hidden}
body{
  position:relative;
  font-family:"Open Sans",Arial,sans-serif;
  background:radial-gradient(ellipse at 50% 45%,var(--backdrop) 40%,var(--backdrop-edge) 100%);
  color:var(--ink);
}
.sheet{position:absolute;background:var(--paper);box-shadow:var(--shadow)}
.brand{font-weight:700;color:var(--navy);text-transform:uppercase;letter-spacing:.02em;display:flex;align-items:center;gap:6px;line-height:1;white-space:nowrap}
.brand .mark{width:9px;height:9px;background:var(--gold);flex:none}

/* Letterhead */
.letterhead{left:34px;top:41px;width:523px;height:686px;padding:0 46px}
.letterhead .head{display:flex;justify-content:space-between;padding-top:34px;height:108px}
.letterhead .brand{font-size:11.5px;margin-top:34px}
.letterhead .address{font-size:7px;line-height:1.45;width:150px;color:var(--ink)}
.contact-list{list-style:none;margin-top:6px}
.contact-list li{display:flex;align-items:center;gap:5px;font-size:6.5px;line-height:1.9;white-space:nowrap}
.contact-list svg{width:7px;height:7px;flex:none}
.rule{height:2px;background:linear-gradient(90deg,var(--navy) 0 70%,var(--gold) 70% 100%);margin:6px 0 0}
.letter{margin-top:46px;font-size:6.3px;line-height:1.75;color:var(--muted)}
.letter .salutation{font-size:12px;color:var(--ink);margin-bottom:20px}
.letter p{margin-bottom:12px}
.signoff{margin-top:26px;font-size:6.3px;color:var(--muted)}
.signature{width:48px;height:18px;margin:8px 0 6px;background:linear-gradient(90deg,#2a2a2a,#777);border-radius:50%;opacity:.6}
.signer{font-size:6.5px;font-weight:700;color:var(--ink);line-height:1.5}
.signer span{display:block;font-weight:400;color:var(--muted);font-size:5.5px}

/* Business card front */
.card-front{left:629px;top:41px;width:264px;height:137px;overflow:hidden}
.card-front .brand{position:absolute;left:14px;top:62px;font-size:6px;gap:4px}
.card-front .brand .mark{width:7px;height:7px}
.card-front .person{position:absolute;left:118px;top:16px;right:8px}
.card-front .name{font-size:10px;font-weight:600;color:var(--navy)}
.card-front .title{font-size:5.3px;color:var(--gold);line-height:1.4;margin-top:2px}
.card-front .contact-list{margin-top:6px}
.card-front .contact-list li{font-size:5px;line-height:1.75}
.card-front .contact-list svg{width:5px;height:5px}
.card-front .band{position:absolute;left:0;right:0;bottom:0;height:10px;background:var(--navy);border-top:2px solid var(--gold)}

/* Business card back */
.card-back{left:905px;top:41px;width:264px;height:137px;background:var(--navy);overflow:hidden}
.card-back .brand{position:absolute;left:36px;top:58px;color:#fff;font-size:12px}
.card-back .site{position:absolute;right:-30px;top:62px;transform:rotate(90deg);font-size:6px;color:#fff;letter-spacing:.1em;text-transform:uppercase}

/* Envelope (back) */
.envelope-back{left:629px;top:271px;width:540px;height:185px;overflow:hidden}
.envelope-back svg.flap{position:absolute;inset:0}
.envelope-back .brand{position:absolute;left:0;right:0;top:66px;justify-content:center;font-size:9px}
.envelope-back .site{position:absolute;left:0;right:0;top:88px;text-align:center;font-size:6.5px;letter-spacing:.12em;color:var(--navy)}

/* Envelope (front) */
.envelope-front{left:629px;top:540px;width:540px;height:187px}
.envelope-front .brand{position:absolute;left:18px;top:34px;font-size:9px}
.envelope-front .return{position:absolute;left:18px;top:52px;font-size:5.8px;line-height:1.5;color:var(--ink)}
</style>
</head>
<body>

<section class="sheet letterhead">
  <header class="head">
    <div class="brand"><span class="mark"></span>Mark Whitfield, Esq., APC</div>
    <div class="address">
      742 S. Milbrook Avenue<br>Alder Springs, CA 90000
      <ul class="contact-list">
        <li><svg viewBox="0 0 10 10"><path d="M2 1h2l1 2-1.2 1a5 5 0 0 0 2.2 2.2L7 5l2 1v2a1 1 0 0 1-1 1A7 7 0 0 1 1 2a1 1 0 0 1 1-1z" fill="#1f2f6b"/></svg>(555) 555-0147</li>
        <li><svg viewBox="0 0 10 10"><rect x="1" y="2" width="8" height="6" fill="#1f2f6b"/><rect x="2.5" y="3" width="5" height="2" fill="#fff"/></svg>(555) 555-0182</li>
        <li><svg viewBox="0 0 10 10"><rect x="1" y="2" width="8" height="6" fill="#1f2f6b"/><path d="M1 2l4 3 4-3" stroke="#fff" fill="none"/></svg>mark@whitfieldlegal.example</li>
        <li><svg viewBox="0 0 10 10"><circle cx="5" cy="5" r="4" fill="#1f2f6b"/><path d="M1 5h8M5 1v8" stroke="#fff" stroke-width=".6"/></svg>www.whitfieldlegal.example</li>
      </ul>
    </div>
  </header>
  <div class="rule"></div>
  <article class="letter">
    <p class="salutation">Dear Mr. Carter,</p>
    <p>Thank you for meeting with our office last week regarding your claim. We have reviewed the medical reports, employer statements and wage records you provided, and we believe your case is strong. Our next step is to file the formal application and request a hearing date before the board.</p>
    <p>Please keep copies of every letter you receive from the insurance carrier and note any missed payments. If your doctor changes your work restrictions, send us the updated report right away so we can share it with the judge.</p>
    <p>We will contact you once the hearing is scheduled. In the meantime, do not sign any settlement papers without first speaking to our office. Feel free to call with any questions about your benefits or the process ahead.</p>
    <p>Thank you for trusting us with your case.</p>
    <div class="signoff">Sincerely,</div>
    <div class="signature" role="img" aria-label="Handwritten signature"></div>
    <div class="signer">Mark Whitfield<span>Attorney at Law/Abogado</span><span>Workers' Compensation Judge (Ret.)</span></div>
  </article>
</section>

<section class="sheet card-front">
  <div class="brand"><span class="mark"></span>Mark Whitfield, Esq., APC</div>
  <div class="person">
    <div class="name">Mark Whitfield</div>
    <div class="title">Attorney at Law/Abogado<br>Workers' Compensation Judge (Ret.)</div>
    <ul class="contact-list">
      <li><svg viewBox="0 0 10 10"><circle cx="5" cy="5" r="4" fill="#1f2f6b"/></svg>742 S. Milbrook Avenue, Alder Springs, CA 90000</li>
      <li><svg viewBox="0 0 10 10"><circle cx="5" cy="5" r="4" fill="#1f2f6b"/></svg>(555) 555-0147</li>
      <li><svg viewBox="0 0 10 10"><circle cx="5" cy="5" r="4" fill="#1f2f6b"/></svg>mark@whitfieldlegal.example</li>
    </ul>
  </div>
  <div class="band"></div>
</section>

<section class="sheet card-back">
  <div class="brand"><span class="mark"></span>Mark Whitfield, Esq., APC</div>
  <div class="site">www.whitfieldlegal.example</div>
</section>

<section class="sheet envelope-back">
  <svg class="flap" viewBox="0 0 540 185" preserveAspectRatio="none">
    <path d="M0 0L270 110 540 0" fill="none" stroke="#e2e2e2" stroke-width="1.5"/>
    <path d="M0 185L230 90M540 185L310 90" fill="none" stroke="#ececec" stroke-width="1"/>
  </svg>
  <div class="brand"><span class="mark"></span>Mark Whitfield, Esq., APC</div>
  <div class="site">www.whitfieldlegal.example</div>
</section>

<section class="sheet envelope-front">
  <div class="brand"><span class="mark"></span>Mark Whitfield, Esq., APC</div>
  <div class="return">742 S. Milbrook Avenue<br>Alder Springs, CA 90000</div>
</section>

</body>
</html>
```